K & D A/C Compressors' Business Card

Hello,

I need someone to create a new business card for my business. The name of my Business is: K & D A/C Compressors. I sell automotive air conditioning parts (a/c parts). I would like the business card to incorporate my logo, and to have an automotive feel to it. It is important that the business card feel like it is coming from an automotive parts business.

I already have a logo, which I will provide.

Thanks.
Updates

Project Deadline Extended Reason: I feel like extending the deadline until October 9, 2017, will allow for more time to design the business card. Thank you for your understanding. Added Monday, October 2, 2017

Target Market(s)

Consumers who need automotive a/c parts, and auto mechanics.

Industry/Entity Type

Automotive

Contact Information for Business Card

Business name: K & D A/C Compressors
Business Address: 48207 Southwest 36th Street, North Miami Beach, Florida 33162
Telephone: 305-472-1390
Fax: To be provided once I choose your design.
Website: www.kdcoolunits.example
Email: support@kdcoolunits.example
Names: To be provided once I choose your design.

Font styles to use
Sans Serif

Colors

Designer to choose colors to be used in the design.

Requirements
Must have
• The business card must include all of the "Business Card Details" and the logo I have uploaded.

```html
<!DOCTYPE html>
<html lang="en">
<head>
<meta charset="utf-8">
<title>K &amp; D A/C Compressors – Business Card</title>
<link rel="stylesheet" href="https://fonts.googleapis.com/css2?family=Montserrat:wght@400;600;700&family=Work+Sans:wght@400;500&display=swap">
<style>
  :root {
    --backdrop: #2a2b2d;
    --card: #141415;
    --card-edge: #1c1c1e;
    --accent: #12a8ec;
    --silver: #c4c6c9;
    --text: #d9dadc;
    --muted: #a9abae;
  }
  * { box-sizing: border-box; margin: 0; padding: 0; }
  html, body { width: 1200px; height: 900px; overflow: hidden; }
  body {
    background: var(--backdrop);
    display: flex;
    flex-direction: column;
    align-items: center;
    justify-content: center;
    gap: 36px;
    font-family: "Work Sans", sans-serif;
  }
  .card {
    position: relative;
    width: 700px;
    height: 400px;
    background: radial-gradient(ellipse at 40% 30%, var(--card-edge), var(--card) 70%);
    box-shadow: 0 14px 30px rgba(0,0,0,0.45);
    overflow: hidden;
  }
  .card__band {
    position: absolute;
    left: 0; right: 0; bottom: 0;
    height: 9px;
    background: var(--accent);
  }
  .brand {
    display: flex;
    align-items: center;
    gap: 14px;
    font-family: "Montserrat", sans-serif;
    font-weight: 600;
    color: var(--silver);
    letter-spacing: 0.5px;
    white-space: nowrap;
  }
  .brand__mark {
    width: 18px; height: 18px;
    background: var(--accent);
    flex: none;
  }
  .card--front .brand {
    position: absolute;
    left: 50%; top: 46%;
    transform: translate(-50%, -50%);
    font-size: 38px;
  }
  .card--back .brand {
    position: absolute;
    left: 36px; top: 183px;
    transform: translateY(-50%);
    font-size: 22px;
    letter-spacing: 0.2px;
    gap: 10px;
  }
  .card--back .brand__mark { width: 13px; height: 13px; }
  .divider {
    position: absolute;
    left: 382px; top: 108px;
    width: 2px; height: 150px;
    background: var(--accent);
  }
  .contact {
    position: absolute;
    left: 406px; top: 110px;
  }
  .contact__name {
    font-family: "Montserrat", sans-serif;
    font-weight: 700;
    font-size: 25px;
    color: var(--accent);
    letter-spacing: 1px;
    text-transform: uppercase;
    line-height: 1;
    white-space: nowrap;
  }
  .contact__role {
    font-size: 15px;
    color: var(--muted);
    margin: 4px 0 14px;
  }
  .contact__list { list-style: none; }
  .contact__item {
    display: flex;
    align-items: center;
    gap: 12px;
    font-size: 16px;
    color: var(--text);
    line-height: 23px;
    white-space: nowrap;
  }
  .contact__item svg {
    width: 13px; height: 13px;
    flex: none;
    fill: none;
    stroke: var(--accent);
    stroke-width: 2;
  }
  .contact__highlight { color: var(--accent); }
  .address {
    position: absolute;
    left: 36px; bottom: 34px;
    font-size: 16px;
    color: var(--text);
    letter-spacing: 0.2px;
    white-space: nowrap;
  }
</style>
</head>
<body>

<section class="card card--front" aria-label="Card front">
  <div class="brand"><span class="brand__mark"></span>K &amp; D A/C Compressors</div>
  <div class="card__band"></div>
</section>

<section class="card card--back" aria-label="Card back">
  <div class="brand"><span class="brand__mark"></span>K &amp; D A/C Compressors</div>
  <div class="divider"></div>
  <div class="contact">
    <h1 class="contact__name">Dean Halvorsen</h1>
    <p class="contact__role">Director</p>
    <ul class="contact__list">
      <li class="contact__item">
        <svg viewBox="0 0 16 16"><path d="M4 1.5l2.5 3-1.6 1.8a9 9 0 0 0 4.8 4.8l1.8-1.6 3 2.5-1.5 2.5C7.5 14.5 1.5 8.5 1.5 3z"/></svg>
        305-472-1390
      </li>
      <li class="contact__item">
        <svg viewBox="0 0 16 16"><rect x="4" y="1.5" width="8" height="4"/><rect x="1.5" y="5.5" width="13" height="6"/><rect x="4" y="9.5" width="8" height="5"/></svg>
        305-472-1391
      </li>
      <li class="contact__item">
        <svg viewBox="0 0 16 16"><rect x="1.5" y="3" width="13" height="10"/><path d="M1.5 3l6.5 6 6.5-6"/></svg>
        support@kdcoolunits.example
      </li>
      <li class="contact__item">
        <svg viewBox="0 0 16 16"><circle cx="8" cy="8" r="6.5"/><ellipse cx="8" cy="8" rx="3" ry="6.5"/><path d="M1.5 8h13"/></svg>
        <span>www.<span class="contact__highlight">kdcoolunits</span>.example</span>
      </li>
    </ul>
  </div>
  <p class="address">48207 Southwest 36th Street, North Miami Beach, Florida 33162</p>
  <div class="card__band"></div>
</section>

</body>
</html>
```